Stationary Package for Construction Company
Modern and Professional
Stationary Package for Construction Company - Construction
Creative Brief
Professional
Karl T. Wentworth
V.P., Operations & Sr. Project Manager
7148 Orchard Lane, Unit 512 Myrtle Beach, SC 29614
843.555.0178 ext. 214
Karl@BrimstackLLC.example
www.BrimstackLLC.example
Current logo is uploaded in .ai format. If color needs to be altered, that is ok. We may also need an alternate color for back of business card. I have also uploaded a few card samples that we already like.
Back of card should be alternate color, either red or black. Two options: One card back with logo only, and one version with logo, web address and services rendered, which I'll specify in greater detail as we narrow down specific designs that we like.

```html
<!DOCTYPE html>
<html lang="en">
<head>
<meta charset="utf-8">
<title>Brimstack Business Card</title>
<link href="https://fonts.googleapis.com/css2?family=Oswald:wght@500;700&family=Open+Sans:wght@400;600&display=swap" rel="stylesheet">
<style>
  :root {
    --bg: #e4e4e4;
    --card: #ffffff;
    --red: #e3161b;
    --ink: #3a3a3a;
    --grey: #9a9a9a;
    --black: #1c1c1c;
    --on-red: #ffffff;
  }
  html, body { margin: 0; padding: 0; overflow: hidden; }
  body {
    width: 1200px; height: 901px;
    background: var(--bg);
    position: relative;
    font-family: "Open Sans", Arial, sans-serif;
  }
  .business-card {
    position: absolute; left: 150px; top: 193px;
    width: 900px; height: 514px;
    background: var(--card);
    box-shadow: 0 10px 30px rgba(0,0,0,.18);
    overflow: hidden;
  }
  .swoosh { position: absolute; inset: 0; width: 100%; height: 100%; }
  .brand {
    position: absolute; left: 70px; top: 140px;
    color: var(--red);
    font-family: "Oswald", Arial, sans-serif;
  }
  .brand-row { display: flex; align-items: center; gap: 16px; }
  .brand-mark { width: 54px; height: 54px; background: var(--red); }
  .brand-name { font-size: 56px; font-weight: 700; letter-spacing: 2px; line-height: 1; }
  .brand-tagline {
    margin-top: 12px; font-size: 22px; font-weight: 500;
    letter-spacing: 3px; color: var(--red);
  }
  .contact {
    position: absolute; right: 50px; top: 30px;
    text-align: right; color: var(--ink);
  }
  .person-name {
    font-family: "Oswald", Arial, sans-serif;
    font-size: 28px; font-weight: 500; color: var(--red);
    letter-spacing: 1px; text-transform: uppercase; line-height: 1.3;
  }
  .person-title { font-size: 16px; margin-bottom: 12px; }
  .contact-line {
    display: flex; justify-content: flex-end; align-items: center;
    gap: 12px; font-size: 15px; margin: 6px 0;
  }
  .contact-line svg { width: 16px; height: 16px; fill: var(--red); }
  .address {
    position: absolute; left: 70px; bottom: 36px;
    font-size: 16px; font-weight: 600; line-height: 1.5;
    color: var(--on-red);
  }
</style>
</head>
<body>
  <div class="business-card">
    <svg class="swoosh" viewBox="0 0 900 514" preserveAspectRatio="none">
      <path d="M0 365 C 330 385, 660 330, 900 245" fill="none" stroke="var(--grey)" stroke-width="6"/>
      <path d="M0 378 C 330 398, 660 343, 900 258" fill="none" stroke="var(--black)" stroke-width="5"/>
      <path d="M0 392 C 330 412, 660 357, 900 272 L900 300 C 650 400, 420 480, 300 514 L0 514 Z" fill="var(--red)"/>
    </svg>

    <div class="brand">
      <div class="brand-row">
        <div class="brand-mark"></div>
        <div class="brand-name">BRIMSTACK</div>
      </div>
      <div class="brand-tagline">QUALITY • SERVICE • PRICE</div>
    </div>

    <div class="contact">
      <div class="person-name">Karl T. Wentworth</div>
      <div class="person-title">Managing Director</div>
      <div class="contact-line">843.555.0178
        <svg viewBox="0 0 24 24"><path d="M6.6 10.8a15 15 0 0 0 6.6 6.6l2.2-2.2a1 1 0 0 1 1-.25 11.4 11.4 0 0 0 3.6.6 1 1 0 0 1 1 1V20a1 1 0 0 1-1 1A17 17 0 0 1 3 4a1 1 0 0 1 1-1h3.5a1 1 0 0 1 1 1c0 1.25.2 2.45.6 3.6a1 1 0 0 1-.25 1z"/></svg>
      </div>
      <div class="contact-line">843.555.0179
        <svg viewBox="0 0 24 24"><rect x="6" y="2" width="12" height="20" rx="2"/></svg>
      </div>
      <div class="contact-line">Karl@BrimstackLLC.example
        <svg viewBox="0 0 24 24"><path d="M2 5h20v14H2z M2 5l10 8 10-8" stroke="#fff" stroke-width="1.5"/></svg>
      </div>
      <div class="contact-line">www.BrimstackLLC.example
        <svg viewBox="0 0 24 24"><circle cx="12" cy="12" r="10"/></svg>
      </div>
    </div>

    <div class="address">7148 Orchard Lane, Unit 512<br>Myrtle Beach</div>
  </div>
</body>
</html>
```